Printer Cartridges Supplier Namecard

Attached is my company logo and the design of my current namecard. I would like to have a more special look for it. Can have a little cuteness too rather than those normal standard feel. I'm a supplier mainly dealing with original and compatible printer toner cartridges, some other products like paper supplies as well.

Target Market(s)

Companies, businesses, corporates

Industry/Entity Type

It Company

Contact Information for Business Card

Logo, name, contact, address, supplies and maybe a slogan

Colors
85cae6
33a6d7
3176b5
0255a3
0792cd
85abd2

Requirements
Must have
• Logo, name, contact and address basic details.
• Must include some pictures, not just rearrange what I'm currently having.
Nice to have
• Be creative and bold, a diiferent traditional feel.

```html
<!DOCTYPE html>
<html lang="en">
<head>
<meta charset="utf-8">
<title>Tonerbay Business Card</title>
<link href="https://fonts.googleapis.com/css2?family=Roboto:wght@400;500;700&display=swap" rel="stylesheet">
<style>
  :root {
    --stage: #7a6352;
    --paper: #f7f7f7;
    --slate: #58595b;
    --sky: #5ab4e5;
    --ink: #4a4a4a;
    --rule: #333333;
    --white: #ffffff;
  }
  * { margin: 0; padding: 0; box-sizing: border-box; }
  html, body { width: 1200px; height: 960px; overflow: hidden; }
  body {
    position: relative;
    background: var(--stage);
    font-family: "Roboto", Arial, sans-serif;
  }
  .card {
    position: absolute;
    width: 600px;
    height: 342px;
    box-shadow: 0 3px 8px rgba(0,0,0,0.35);
  }
  .card-front { left: 302px; top: 129px; background: var(--paper); }
  .card-back { left: 299px; top: 488px; background: var(--slate); }

  .brand {
    position: absolute;
    left: 40px; top: 40px;
    display: flex; align-items: center; gap: 12px;
  }
  .brand-mark {
    width: 30px; height: 30px;
    background: var(--sky);
    border-radius: 4px;
  }
  .brand-name {
    font-size: 40px; font-weight: 400;
    color: var(--ink);
    letter-spacing: -0.5px;
  }
  .side-tab {
    position: absolute;
    right: 0; top: 175px;
    width: 9px; height: 34px;
    background: var(--sky);
    border-radius: 6px 0 0 6px;
  }
  .person {
    position: absolute;
    right: 40px; top: 171px;
    text-align: right;
  }
  .person-name {
    font-size: 20px; font-weight: 700;
    color: var(--sky);
    text-transform: uppercase;
    letter-spacing: 0.2px;
  }
  .person-role {
    font-size: 15px; font-weight: 500;
    color: var(--ink);
    margin-top: 2px;
  }
  .divider {
    position: absolute;
    left: 40px; right: 40px; top: 229px;
    height: 1px; background: var(--rule);
  }
  .contacts {
    position: absolute;
    left: 38px; top: 246px;
    list-style: none;
    font-size: 14px; color: var(--ink);
    line-height: 18px;
  }
  .contacts li { display: flex; align-items: center; gap: 6px; }
  .contacts svg { width: 14px; height: 14px; fill: var(--sky); flex: none; }
  .address {
    position: absolute;
    right: 38px; top: 248px;
    text-align: right;
    font-style: normal;
    font-size: 14px; color: var(--ink);
    line-height: 18px;
  }

  .back-emblem {
    position: absolute;
    left: 200px; top: 57px;
    width: 200px; height: 200px;
    border-radius: 50%;
    background: var(--sky);
  }
  .services {
    position: absolute;
    left: 0; right: 0; top: 272px;
    text-align: center;
    color: var(--white);
    font-size: 15px;
    line-height: 18px;
  }
  .services .dot {
    display: inline-block;
    width: 5px; height: 5px;
    border-radius: 50%;
    background: var(--sky);
    vertical-align: middle;
    margin: 0 2px;
  }
</style>
</head>
<body>
  <section class="card card-front">
    <div class="brand">
      <span class="brand-mark"></span>
      <span class="brand-name">tonerbay</span>
    </div>
    <span class="side-tab"></span>
    <div class="person">
      <div class="person-name">Maren Tay</div>
      <div class="person-role">Sales Executive</div>
    </div>
    <div class="divider"></div>
    <ul class="contacts">
      <li>
        <svg viewBox="0 0 16 16" aria-hidden="true"><path d="M3.6 1.2l2.3 2.6c.4.4.3 1-.1 1.4L4.7 6.3c.9 2 2.6 3.8 4.9 4.9l1.1-1.1c.4-.4 1-.4 1.4-.1l2.6 2.2c.4.4.4 1 0 1.4l-1.3 1.3c-.6.6-1.5.8-2.3.5C6.3 13.8 2.2 9.7.6 5c-.3-.8-.1-1.7.5-2.3L2.2 1.2c.4-.4 1-.4 1.4 0z"/></svg>
        HP 9000 4127
      </li>
      <li>
        <svg viewBox="0 0 16 16" aria-hidden="true"><path d="M1 3h14v1.2L8 9 1 4.2z"/><path d="M1 5.6l7 4.8 7-4.8V13H1z"/></svg>
        maren@tonerbay.sg
      </li>
      <li>
        <svg viewBox="0 0 16 16" aria-hidden="true"><circle cx="8" cy="8" r="7"/><path d="M4 5c1 0 2 1 3 1s1 2 0 3-1 2-2 3M10 3c0 1 1 2 2 2s1 2 2 2M9 11c1-1 2 0 3 1" stroke="#f7f7f7" stroke-width="1.2" fill="none"/></svg>
        www.tonerbay.sg
      </li>
    </ul>
    <address class="address">
      415A Willow Grove Crescent<br>
      #06-112<br>
      Singapore 540415
    </address>
  </section>

  <section class="card card-back">
    <span class="back-emblem"></span>
    <p class="services">
      Printer Ink &amp; Toner Cartridges <span class="dot"></span> Original Printer Cartridges<br>
      Paper Products <span class="dot"></span> Printer Maintainence &amp; Repair
    </p>
  </section>
</body>
</html>
```